Serlivo Business Cards

We need new Business Cards for our startup. It just launched.It is working in the high-end it-market. Specifically in the cloud area. We are a hybrid cloud company. The company logo is attached. We are a Swiss based company. Information visible on the card is: 1. Logo 2. Company Name: Serlivo AG 3. Subtitle: Hybrid Clouds. 3. Name: Tobias Ferrand 4. Adress: Lindenhofweg 14a, 8640 Rapperswil, Switzerland 5. Email: tobias@serlivo-mail.ch. 6. Mobile: +41 79 386 42 15. It should be a grey/white design. Similar to the attached logo. It should have class, high-quality but not too much color and no gold used.
Updates

I forgot to add my Position. Please use Founder / CEO. thanks tobias

Industry/Entity Type

Business

```html
<!DOCTYPE html>
<html lang="en">
<head>
<meta charset="utf-8">
<title>Serlivo AG – Business Card</title>
<link rel="stylesheet" href="https://fonts.googleapis.com/css2?family=Lato:wght@400;700&display=swap">
<style>
  :root {
    --page-bg: #e7e5e2;
    --card-edge: #b9b6b2;
    --panel-dark: #1f1f22;
    --panel-mid: #2c2c30;
    --band-grey: #5b5a5a;
    --band-silver: #d6d3cf;
    --name-tone: #cdc4b4;
    --text-light: #d9dce3;
    --text-soft: #b9bcc4;
    --wordmark: #4b4b4d;
  }
  html, body {
    margin: 0;
    padding: 0;
    width: 1200px;
    height: 970px;
    overflow: hidden;
    background: var(--page-bg);
  }
  .card {
    position: absolute;
    left: 80px;
    top: 195px;
    width: 1040px;
    height: 580px;
    box-shadow: 0 18px 40px rgba(0,0,0,0.18);
  }
  .card svg { display: block; width: 100%; height: 100%; }
  .card-text { font-family: 'Lato', sans-serif; }
  .wordmark { fill: var(--wordmark); font-size: 24px; font-weight: 400; letter-spacing: 0.32em; }
  .holder-name { fill: var(--name-tone); font-size: 21px; font-weight: 700; letter-spacing: 0.02em; }
  .holder-role { fill: var(--name-tone); font-size: 17.5px; font-weight: 400; }
  .address-line, .contact-line { fill: var(--text-light); font-size: 17.5px; font-weight: 400; }
  .company-name { fill: var(--name-tone); font-size: 22px; font-weight: 700; }
  .company-tagline { fill: var(--text-soft); font-size: 17.5px; font-weight: 400; }
  .contact-icon { fill: none; stroke: var(--text-soft); stroke-width: 1.3; }
</style>
</head>
<body>
  <div class="card">
    <svg viewBox="0 0 753 420" preserveAspectRatio="none" xmlns="http://www.w3.org/2000/svg">
      <defs>
        <linearGradient id="frostTone" x1="0" y1="0" x2="0" y2="1">
          <stop offset="0" stop-color="#ece9e6"/>
          <stop offset="0.45" stop-color="#f3f1ee"/>
          <stop offset="0.8" stop-color="#e3ccd0"/>
          <stop offset="1" stop-color="#d9d2cd"/>
        </linearGradient>
        <linearGradient id="panelShade" x1="0" y1="0" x2="1" y2="1">
          <stop offset="0" stop-color="var(--panel-mid)"/>
          <stop offset="1" stop-color="var(--panel-dark)"/>
        </linearGradient>
      </defs>

      <rect class="frost-surface" x="0" y="0" width="753" height="420" fill="url(#frostTone)" role="img" aria-label="Frosted translucent card surface"/>

      <path class="band-grey" d="M340,0 C410,110 410,310 335,420 L753,420 L753,0 Z" fill="var(--band-grey)"/>
      <path class="band-silver" d="M352,0 C424,110 422,310 347,420" fill="none" stroke="var(--band-silver)" stroke-width="2.2"/>
      <path class="panel-dark" d="M372,0 C445,110 440,310 362,420 L753,420 L753,0 Z" fill="url(#panelShade)"/>
      <path class="panel-edge" d="M378,0 C451,110 446,310 368,420" fill="none" stroke="#8a8784" stroke-width="1"/>

      <g class="card-text">
        <circle class="wordmark-dot" cx="160" cy="205" r="11" fill="var(--wordmark)"/>
        <text class="wordmark" x="184" y="214">SERLIVO</text>

        <text class="holder-name" x="483" y="123">TOBIAS FERRAND</text>
        <text class="holder-role" x="483" y="146">Founder / CEO</text>

        <text class="address-line" x="484" y="204">Lindenhofweg 14a</text>
        <text class="address-line" x="484" y="226">8640 Rapperswil, Switzerland</text>

        <rect class="contact-icon" x="489" y="249" width="9" height="16" rx="1.6"/>
        <text class="contact-line" x="513" y="264">+41 79 386 42 15</text>
        <rect class="contact-icon" x="487" y="277" width="13" height="9"/>
        <path class="contact-icon" d="M487,277 L493.5,282.5 L500,277"/>
        <text class="contact-line" x="513" y="286">tobias@serlivo-mail.ch</text>

        <text x="443" y="383"><tspan class="company-name">SERLIVO AG - </tspan><tspan class="company-tagline">Hybrid Clouds</tspan></text>
      </g>

      <rect class="card-edge" x="0.5" y="0.5" width="752" height="419" fill="none" stroke="var(--card-edge)" stroke-width="1"/>
    </svg>
  </div>
</body>
</html>
```